I need a flyer designed for a marine service company. Our company specializes in boat engine diagnostic/repair, engine service, electronic installation and repairs, bottom paint, detailing, winterization and shrink wrapping. We would like to see designs that incorporate our color scheme of deep blue, blueish gray and black (please see attached photo)

Target Market(s)

Boat owners

Industry/Entity Type

Marine

Logo Text

Kelpwick Harbor Marine Services

Requirements
Must have
• Company logo
Nice to have
• List the services we provide.

```html
<!DOCTYPE html>
<html lang="en">
<head>
<meta charset="utf-8">
<title>Kelpwick Harbor Marine Services – Flyer</title>
<link rel="stylesheet" href="https://fonts.googleapis.com/css2?family=Noto+Serif:wght@400;700&family=Archivo:wght@700&family=Oswald:wght@500&family=Nunito+Sans:wght@600&display=swap">
<style>
  :root {
    --navy: #16264a;
    --steel-blue: #4b6aa3;
    --mist: #dfe8ef;
    --paper: #f3f3f3;
    --white: #ffffff;
    --ink: #111a2e;
  }
  * { box-sizing: border-box; margin: 0; padding: 0; }
  html, body { width: 686px; height: 1200px; overflow: hidden; background: var(--white); }
  .flyer { position: relative; width: 686px; height: 1200px; overflow: hidden; background: var(--paper); }
  .hero-art { position: absolute; left: 0; top: 0; width: 686px; height: 780px; display: block; }

  .brand-mark { position: absolute; left: 30px; top: 56px; width: 126px; text-align: center; }
  .brand-mark__circle { width: 84px; height: 84px; margin: 0 auto 8px; border: 3px solid var(--navy); border-radius: 50%; }
  .brand-mark__name { font-family: "Noto Serif", serif; font-weight: 400; font-size: 12px; line-height: 1.25; color: var(--navy); letter-spacing: 0.5px; }

  .title { position: absolute; left: 178px; top: 62px; width: 490px; font-family: "Noto Serif", serif; }
  .title__main { display: block; font-weight: 700; font-size: 41px; line-height: 1; color: var(--ink); letter-spacing: 0.5px; }
  .title__sub { display: block; font-weight: 400; font-size: 41px; line-height: 1.1; color: var(--steel-blue); }

  .services-tab { position: absolute; left: 223px; top: 776px; width: 240px; height: 40px; background: var(--steel-blue); color: var(--white); border-radius: 0 0 8px 8px; font-family: "Noto Serif", serif; font-weight: 700; font-size: 22px; line-height: 40px; text-align: center; letter-spacing: 1px; }
  .services-tab::before, .services-tab::after { content: ""; position: absolute; top: -6px; width: 12px; height: 12px; background: var(--navy); }
  .services-tab::before { left: -6px; transform: skewX(-20deg); }
  .services-tab::after { right: -6px; transform: skewX(20deg); }

  .services { position: absolute; top: 842px; list-style: none; }
  .services--left { left: 70px; }
  .services--right { left: 458px; }
  .service { display: flex; align-items: center; height: 46px; font-family: "Archivo", sans-serif; font-weight: 700; font-size: 13.5px; color: var(--ink); }
  .service__icon { width: 26px; height: 26px; margin-right: 11px; flex: none; }

  .footer-art { position: absolute; left: 0; top: 1030px; width: 686px; height: 170px; display: block; }
  .contact-pill { position: absolute; left: 227px; top: 1036px; width: 230px; height: 42px; border-radius: 21px; background: var(--navy); color: var(--white); font-family: "Noto Serif", serif; font-weight: 700; font-size: 21px; line-height: 42px; text-align: center; letter-spacing: 1px; }

  .contact-row { position: absolute; left: 26px; right: 18px; top: 1128px; display: flex; align-items: center; color: var(--white); font-style: normal; }
  .contact-row__phone { display: flex; align-items: center; font-family: "Oswald", sans-serif; font-weight: 500; font-size: 26px; letter-spacing: 0.5px; margin-right: 26px; }
  .contact-row__phone svg { width: 22px; height: 22px; margin-right: 10px; }
  .contact-row__item { display: flex; align-items: center; font-family: "Nunito Sans", sans-serif; font-weight: 600; font-size: 11px; margin-right: 24px; }
  .contact-row__item:last-child { margin-right: 0; }
  .contact-row__item svg { width: 11px; height: 11px; margin-right: 8px; }
</style>
</head>
<body>
<main class="flyer">
  <svg class="hero-art" viewBox="0 0 686 780" xmlns="http://www.w3.org/2000/svg">
    <defs>
      <linearGradient id="sky" x1="0" y1="0" x2="0" y2="1">
        <stop offset="0" stop-color="#f7fafc"/>
        <stop offset="0.6" stop-color="#e4ecf2"/>
        <stop offset="1" stop-color="#c7d5e0"/>
      </linearGradient>
      <linearGradient id="harbor" x1="0" y1="0" x2="0" y2="1">
        <stop offset="0" stop-color="#c3d0da"/>
        <stop offset="0.12" stop-color="#aebbc6"/>
        <stop offset="0.16" stop-color="#5d6b78"/>
        <stop offset="0.24" stop-color="#7c848a"/>
        <stop offset="0.3" stop-color="#9fb2bf"/>
        <stop offset="0.55" stop-color="#6e96ab"/>
        <stop offset="0.8" stop-color="#4d7d96"/>
        <stop offset="1" stop-color="#3a6881"/>
      </linearGradient>
      <radialGradient id="hull-glow" cx="0.5" cy="0.5" r="0.5">
        <stop offset="0" stop-color="#f4f7f9" stop-opacity="0.95"/>
        <stop offset="0.6" stop-color="#e3eaef" stop-opacity="0.6"/>
        <stop offset="1" stop-color="#e3eaef" stop-opacity="0"/>
      </radialGradient>
      <radialGradient id="workshop" cx="0.5" cy="0.4" r="0.6">
        <stop offset="0" stop-color="#8d9aa0"/>
        <stop offset="0.45" stop-color="#3f5670"/>
        <stop offset="0.75" stop-color="#2f6a45"/>
        <stop offset="1" stop-color="#4fb35c"/>
      </radialGradient>
      <radialGradient id="panel" cx="0.4" cy="0.4" r="0.7">
        <stop offset="0" stop-color="#f2f2f0"/>
        <stop offset="0.5" stop-color="#c9c6c2"/>
        <stop offset="0.8" stop-color="#a2836f"/>
        <stop offset="1" stop-color="#5b5a60"/>
      </radialGradient>
      <radialGradient id="garage" cx="0.5" cy="0.35" r="0.65">
        <stop offset="0" stop-color="#b44a42"/>
        <stop offset="0.5" stop-color="#6a3a3c"/>
        <stop offset="1" stop-color="#2c2e35"/>
      </radialGradient>
    </defs>
    <rect width="686" height="780" fill="url(#sky)"/>
    <g class="hero-photo" role="img" aria-label="Photo of a white motor yacht moored in a calm marina beside a breakwater">
      <rect x="0" y="236" width="686" height="400" fill="url(#harbor)"/>
      <ellipse cx="330" cy="390" rx="230" ry="90" fill="url(#hull-glow)"/>
      <ellipse cx="60" cy="410" rx="80" ry="40" fill="url(#hull-glow)"/>
    </g>
    <path d="M0,600 C60,560 130,530 230,545 C330,560 420,610 520,590 C600,575 650,540 686,520 L686,780 L0,780 Z" fill="#ffffff"/>
    <rect x="0" y="776" width="686" height="4" fill="var(--paper)"/>
    <path d="M0,640 C80,590 170,575 260,590 C360,606 430,650 560,660 L560,672 C430,665 350,622 260,612 C170,602 80,615 0,680 Z" fill="#16264a"/>
    <path d="M0,690 C90,625 180,620 270,630 C370,642 440,690 540,690 L540,700 C440,705 360,658 270,650 C180,642 90,660 0,710 Z" fill="#4b6aa3"/>
    <path d="M560,690 C600,685 630,680 640,672 L640,676 C630,686 600,692 560,694 Z" fill="#16264a"/>

    <circle cx="116" cy="600" r="80" fill="#ffffff"/>
    <circle cx="116" cy="600" r="75" fill="none" stroke="#16264a" stroke-width="4"/>
    <circle cx="116" cy="600" r="67" fill="url(#workshop)" role="img" aria-label="Photo of a mechanic servicing a boat engine in a workshop"/>

    <circle cx="314" cy="607" r="78" fill="#ffffff"/>
    <circle cx="314" cy="607" r="73" fill="none" stroke="#16264a" stroke-width="4"/>
    <circle cx="314" cy="607" r="65" fill="url(#panel)" role="img" aria-label="Photo of hands wiring an electrical panel"/>

    <circle cx="497" cy="655" r="72" fill="#ffffff"/>
    <circle cx="497" cy="655" r="67" fill="none" stroke="#16264a" stroke-width="4"/>
    <circle cx="497" cy="655" r="59" fill="url(#garage)" role="img" aria-label="Photo of a technician repairing engine parts"/>
  </svg>

  <div class="brand-mark">
    <div class="brand-mark__circle"></div>
    <p class="brand-mark__name">KELPWICK HARBOR</p>
  </div>

  <h1 class="title">
    <span class="title__main">KELPWICK HARBOR</span>
    <span class="title__sub">MARINE SERVICES</span>
  </h1>

  <h2 class="services-tab">OUR SERVICES</h2>

  <ul class="services services--left">
    <li class="service"><svg class="service__icon" viewBox="0 0 26 26"><circle cx="13" cy="13" r="11.5" fill="none" stroke="#16264a" stroke-width="1.5"/><circle cx="13" cy="13" r="5" fill="none" stroke="#4b6aa3" stroke-width="2"/><path d="M16.5,16.5 L20,20" stroke="#4b6aa3" stroke-width="2"/></svg>BOAT ENGINE DIAGNOSTIC/REPAIR</li>
    <li class="service"><svg class="service__icon" viewBox="0 0 26 26"><circle cx="13" cy="13" r="11.5" fill="none" stroke="#16264a" stroke-width="1.5"/><circle cx="13" cy="13" r="6" fill="none" stroke="#4b6aa3" stroke-width="2.5" stroke-dasharray="2.5 1.5"/><circle cx="13" cy="13" r="2" fill="#4b6aa3"/></svg>ENGINE SERVICE</li>
    <li class="service"><svg class="service__icon" viewBox="0 0 26 26"><circle cx="13" cy="13" r="11.5" fill="none" stroke="#16264a" stroke-width="1.5"/><rect x="7.5" y="7.5" width="11" height="11" rx="1.5" fill="none" stroke="#4b6aa3" stroke-width="2"/><circle cx="13" cy="13" r="2.5" fill="#4b6aa3"/></svg>ELECTRONIC INSTALLATION AND REPAIRS</li>
    <li class="service"><svg class="service__icon" viewBox="0 0 26 26"><circle cx="13" cy="13" r="11.5" fill="none" stroke="#16264a" stroke-width="1.5"/><path d="M8,18 L14,12" stroke="#4b6aa3" stroke-width="2.5" stroke-linecap="round"/><rect x="13" y="7" width="6" height="6" rx="1" fill="#4b6aa3" transform="rotate(45 16 10)"/></svg>SHRINK WRAPPING</li>
  </ul>

  <ul class="services services--right">
    <li class="service"><svg class="service__icon" viewBox="0 0 26 26"><circle cx="13" cy="13" r="11.5" fill="none" stroke="#16264a" stroke-width="1.5"/><rect x="8" y="6.5" width="9" height="12" rx="1" fill="none" stroke="#4b6aa3" stroke-width="1.8"/><path d="M10,10 H15 M10,13 H15 M10,16 H13" stroke="#4b6aa3" stroke-width="1.4"/></svg>DETAILING</li>
    <li class="service"><svg class="service__icon" viewBox="0 0 26 26"><circle cx="13" cy="13" r="11.5" fill="none" stroke="#16264a" stroke-width="1.5"/><path d="M13,6 V20 M7,9.5 L19,16.5 M7,16.5 L19,9.5" stroke="#4b6aa3" stroke-width="1.8" stroke-linecap="round"/></svg>WINTERIZATION</li>
    <li class="service"><svg class="service__icon" viewBox="0 0 26 26"><circle cx="13" cy="13" r="11.5" fill="none" stroke="#16264a" stroke-width="1.5"/><rect x="7.5" y="7.5" width="11" height="11" rx="2" fill="none" stroke="#4b6aa3" stroke-width="1.8"/><path d="M10,7.5 V18.5" stroke="#4b6aa3" stroke-width="1.4"/></svg>SHRINK WRAPPING</li>
  </ul>

  <svg class="footer-art" viewBox="0 0 686 170" xmlns="http://www.w3.org/2000/svg">
    <path d="M0,10 C180,60 380,78 686,52 L686,170 L0,170 Z" fill="#16264a"/>
    <path d="M230,72 C420,78 560,55 686,20 L686,44 C560,72 420,84 230,72 Z" fill="#4b6aa3"/>
  </svg>

  <a class="contact-pill">CONTACT US</a>

  <address class="contact-row">
    <span class="contact-row__phone"><svg viewBox="0 0 24 24"><path d="M6.6,2.5 L9.5,2 L11,7 L8.6,8.6 C9.7,11.4 12.5,14.2 15.4,15.4 L17,13 L22,14.5 L21.5,17.4 C21.2,19.5 19.5,21 17.4,21 C9,21 3,15 3,6.6 C3,4.5 4.5,2.8 6.6,2.5 Z" fill="#ffffff"/></svg>+1 555-014-2277</span>
    <span class="contact-row__item"><svg viewBox="0 0 12 12"><rect x="0.5" y="2" width="11" height="8" fill="none" stroke="#ffffff" stroke-width="1.2"/><path d="M0.5,2 L6,6.5 L11.5,2" fill="none" stroke="#ffffff" stroke-width="1.2"/></svg>kelpwickmarine@mailbox.test</span>
    <span class="contact-row__item"><svg viewBox="0 0 12 12"><circle cx="6" cy="6" r="5.5" fill="#ffffff"/></svg>chat.kelpwickharbor.test</span>
  </address>
</main>
</body>
</html>
```